Brightfen Landscaping Folder Design

I need a graphic designer to design a folder so we can insert informational sheets inside it for customers. The folder must include the company logo, project images, on front and back of folder and slogan " The Experience You Want, The Service You Expect, And The Value You Deserve'

Folder to also include phone numbers : 647 392 5180 as well as the website: www.brightfenlandscaping.example as well as we gurantee a 24 month warranty.

I have attached sample of size we need.

Pixel Harbor has also done something similar for me for Juniper Yards

Target Market(s)

geared toward home owners & commercial/industrial

Industry/Entity Type

Landscaping

Font styles to use
Other font styles liked:
• open to new trendy font

Requirements
Must have
• Telephone Number, email address, slogan, images,
Nice to have
• images of completed projects incorporated into the front and back of folder as well as the logo
Should not have
• n/a

```html
<!DOCTYPE html>
<html lang="en">
<head>
<meta charset="utf-8">
<title>Brightfen Landscaping Folder</title>
<link rel="stylesheet" href="https://fonts.googleapis.com/css2?family=Oswald:wght@500;700&family=Roboto:wght@400;700&display=swap">
<style>
  :root {
    --canvas: #e9e9e6;
    --paper: #ffffff;
    --green: #4cae3f;
    --green-dark: #3f9a34;
    --ink: #2f2f2f;
    --stone: #a9aaa6;
    --stone-dark: #6f716d;
    --pool: #2f6fd0;
    --sky: #c9d2dc;
  }
  * { box-sizing: border-box; margin: 0; padding: 0; }
  html, body { width: 1200px; height: 848px; overflow: hidden; }
  body {
    background: var(--canvas);
    font-family: "Roboto", Arial, sans-serif;
    position: relative;
  }
  .panel {
    position: absolute;
    top: 114px;
    width: 420px;
    height: 620px;
    background: var(--paper);
    box-shadow: 0 6px 18px rgba(0,0,0,.18);
    overflow: hidden;
  }
  .panel--front { left: 150px; }
  .panel--back { left: 630px; }

  /* front */
  .brand {
    position: absolute;
    top: 118px;
    left: 0;
    width: 100%;
    display: flex;
    align-items: center;
    justify-content: center;
    gap: 8px;
    font-family: "Oswald", sans-serif;
    font-weight: 700;
    font-size: 21px;
    letter-spacing: 1px;
    text-transform: uppercase;
    color: var(--ink);
  }
  .brand__mark { width: 12px; height: 12px; background: var(--ink); }
  .slogan {
    position: absolute;
    top: 182px;
    left: 0;
    width: 100%;
    text-align: center;
    font-family: "Oswald", sans-serif;
    font-weight: 700;
    font-size: 34px;
    line-height: 1.02;
    text-transform: uppercase;
  }
  .slogan__line--green { color: var(--green); }
  .slogan__line--ink { color: var(--ink); }
  .pocket-photo { position: absolute; left: 0; bottom: 0; width: 420px; height: 230px; }

  /* back */
  .collage { position: absolute; inset: 12px 12px 0 12px; }
  .contact {
    position: absolute;
    left: 0; right: 0;
    bottom: 92px;
    text-align: center;
    color: #fff;
  }
  .contact__warranty {
    font-family: "Oswald", sans-serif;
    font-weight: 500;
    font-size: 19px;
    letter-spacing: .6px;
    text-transform: uppercase;
  }
  .contact__rule {
    width: 250px;
    height: 1px;
    background: rgba(255,255,255,.7);
    margin: 8px auto 8px;
  }
  .contact__details {
    display: flex;
    justify-content: center;
    gap: 14px;
    font-size: 12px;
  }
  .contact__item { display: flex; align-items: center; gap: 5px; }
  .contact__icon { width: 13px; height: 13px; }
</style>
</head>
<body>

<section class="panel panel--front">
  <div class="brand"><span class="brand__mark"></span>Brightfen Landscaping</div>
  <h1 class="slogan">
    <div class="slogan__line--green">The Experience</div>
    <div class="slogan__line--ink">You Want,</div>
    <div class="slogan__line--green">The Service</div>
    <div class="slogan__line--ink">You Expect,</div>
    <div class="slogan__line--green">And The Value</div>
    <div class="slogan__line--ink">You Deserve</div>
  </h1>
  <svg class="pocket-photo" viewBox="0 0 420 230" role="img" aria-label="Photo of a finished curved concrete driveway in front of a home with autumn trees">
    <defs>
      <linearGradient id="drivewayTone" x1="0" y1="0" x2="0" y2="1">
        <stop offset="0" stop-color="#5e6652"/>
        <stop offset=".45" stop-color="#8d8f86"/>
        <stop offset="1" stop-color="#dcdcd8"/>
      </linearGradient>
    </defs>
    <polygon points="0,110 270,185 420,30 420,230 0,230" fill="url(#drivewayTone)"/>
  </svg>
</section>

<section class="panel panel--back">
  <svg class="collage" viewBox="0 0 396 608" preserveAspectRatio="none">
    <defs>
      <linearGradient id="patioTone" x1="0" y1="0" x2="1" y2="1">
        <stop offset="0" stop-color="#6f7a5c"/><stop offset="1" stop-color="#b9b8b2"/>
      </linearGradient>
      <linearGradient id="poolTone" x1="0" y1="0" x2="0" y2="1">
        <stop offset="0" stop-color="#3b4133"/><stop offset=".5" stop-color="var(--pool)"/><stop offset="1" stop-color="#8da6c6"/>
      </linearGradient>
      <linearGradient id="garageTone" x1="0" y1="0" x2="0" y2="1">
        <stop offset="0" stop-color="#e2ded4"/><stop offset="1" stop-color="#b8ae9c"/>
      </linearGradient>
      <linearGradient id="lotTone" x1="0" y1="0" x2="0" y2="1">
        <stop offset="0" stop-color="var(--sky)"/><stop offset=".4" stop-color="#8b8f92"/><stop offset="1" stop-color="#5d5f5c"/>
      </linearGradient>
    </defs>
    <rect x="0" y="0" width="396" height="160" fill="url(#patioTone)" role="img" aria-label="Photo of stone patio steps with garden plantings"/>
    <rect x="0" y="160" width="200" height="150" fill="url(#poolTone)" role="img" aria-label="Photo of a lit backyard pool with stone surround at dusk"/>
    <rect x="200" y="140" width="196" height="140" fill="url(#garageTone)" role="img" aria-label="Photo of an interlock driveway leading to a garage"/>
    <rect x="80" y="280" width="316" height="190" fill="url(#lotTone)" role="img" aria-label="Photo of a commercial parking lot paving project"/>
    <rect x="0" y="310" width="80" height="160" fill="#6f716d" role="img" aria-label="Photo of paved commercial grounds"/>
    <polygon points="0,420 200,470 396,320 396,608 0,608" fill="var(--green)"/>
  </svg>
  <div class="contact">
    <p class="contact__warranty">We gurantee a 24 month warranty</p>
    <div class="contact__rule"></div>
    <div class="contact__details">
      <span class="contact__item">
        <svg class="contact__icon" viewBox="0 0 16 16"><circle cx="8" cy="8" r="8" fill="rgba(255,255,255,.35)"/><path d="M5.2 4h1.6l.8 2-1 .8a5 5 0 0 0 2.6 2.6l.8-1 2 .8v1.6c0 .6-.5 1-1 1A7 7 0 0 1 4.2 5c0-.5.4-1 1-1z" fill="#fff"/></svg>
        647 392 5180
      </span>
      <span class="contact__item">
        <svg class="contact__icon" viewBox="0 0 16 16"><circle cx="8" cy="8" r="8" fill="rgba(255,255,255,.35)"/><circle cx="8" cy="8" r="4.5" fill="none" stroke="#fff" stroke-width="1"/><path d="M3.5 8h9M8 3.5c-2 2.5-2 6.5 0 9M8 3.5c2 2.5 2 6.5 0 9" fill="none" stroke="#fff" stroke-width="1"/></svg>
        www.brightfenlandscaping.example
      </span>
    </div>
  </div>
</section>

</body>
</html>
```